Display Ad for Local Publication

We have never advertised before but now I would like to have an ad running in our local, community magazine. Our business is Brackwater Mini Storage located in Port Ludlow, WA. PL is a small community (+/-2,500 people located across the Puget Sound from Seattle. The monthly magazine, The Herald, covers all kinds of local news and activities and carries a number of ads from local businesses. Our is the only mini storage in Port Ludlow. We have enclosed storage units of various sizes and outdoor parking spaces for boats, trailers and RVs. I am enclosing a business card and the size requirements for Herald advertisements. I want to develop a 1/8 page ad.

```html
<!DOCTYPE html>
<html lang="en">
<head>
<meta charset="utf-8">
<title>Brackwater Mini Storage – Display Ad</title>
<link rel="stylesheet" href="https://fonts.googleapis.com/css2?family=Bebas+Neue&family=Noto+Serif:wght@700&family=Poppins:wght@400;500;700&display=swap">
<style>
  :root {
    --brand-green: #049a36;
    --band-green: #0a9c3a;
    --photo-light: #3fa96c;
    --photo-mid: #2a8c55;
    --photo-dark: #1d7040;
    --ink: #333333;
    --black: #000000;
    --white: #ffffff;
  }
  * { box-sizing: border-box; margin: 0; padding: 0; }
  html, body { width: 1200px; height: 816px; overflow: hidden; background: var(--white); }
  .ad {
    position: relative;
    width: 1200px;
    height: 816px;
    overflow: hidden;
    font-family: "Poppins", sans-serif;
  }
  .ad-shapes { position: absolute; inset: 0; }
  .business-name {
    position: absolute;
    top: 20px; left: 0; width: 1200px;
    text-align: center;
    font-family: "Noto Serif", serif;
    font-weight: 700;
    font-size: 82px;
    line-height: 1;
    color: var(--white);
    white-space: nowrap;
  }
  .headline {
    position: absolute;
    top: 150px; left: 66px;
    font-weight: 700;
    font-size: 91px;
    line-height: 88px;
    letter-spacing: -1.5px;
    color: var(--ink);
    white-space: nowrap;
  }
  .call-now {
    position: absolute;
    top: 379px; left: 165px; width: 200px;
    text-align: center;
    font-family: "Bebas Neue", sans-serif;
    font-size: 84px;
    line-height: 76px;
    color: var(--white);
  }
  .features {
    position: absolute;
    top: 152px; left: 788px;
    list-style: none;
    color: var(--white);
    font-weight: 500;
    font-size: 37px;
    line-height: 40px;
    letter-spacing: 0.5px;
  }
  .features li { position: relative; padding-left: 23px; margin-bottom: 19px; }
  .features li::before {
    content: "";
    position: absolute; left: 0; top: 16px;
    width: 8px; height: 8px; border-radius: 50%;
    background: var(--white);
  }
  .address {
    position: absolute;
    top: 632px; left: 176px;
    font-style: normal;
    font-size: 32px;
    line-height: 35px;
    letter-spacing: 1px;
    color: var(--white);
    white-space: nowrap;
  }
  .contact {
    position: absolute;
    top: 640px; left: 805px;
    color: var(--white);
    white-space: nowrap;
  }
  .contact-label { font-size: 35px; line-height: 1; letter-spacing: 1.5px; }
  .contact-phone { margin-top: 6px; font-size: 54px; font-weight: 700; line-height: 1; letter-spacing: 1px; }
</style>
</head>
<body>
<div class="ad">
  <svg class="ad-shapes" width="1200" height="816" viewBox="0 0 1200 816">
    <defs>
      <linearGradient id="photoTone" x1="0" y1="0" x2="0" y2="1">
        <stop offset="0" stop-color="#3fa96c"/>
        <stop offset="0.55" stop-color="#2a8c55"/>
        <stop offset="1" stop-color="#1d7040"/>
      </linearGradient>
    </defs>

    <rect class="storage-photo" role="img" aria-label="Covered outdoor parking lot with RVs and trailers stored under a metal roof" x="0" y="0" width="1200" height="816" fill="url(#photoTone)"/>

    <rect class="top-band" x="0" y="0" width="1200" height="128" fill="var(--band-green)"/>

    <path class="wave-band" d="M0,127 H740 Q762,127 762,149 V328 C600,395 420,445 270,462 C160,470 70,448 0,424 Z" fill="var(--brand-green)"/>
    <path class="wave-panel" d="M0,127 H740 Q762,127 762,149 V314 C600,381 420,431 270,448 C160,456 70,434 0,410 Z" fill="var(--white)"/>

    <path class="side-band" d="M1108,254 V150 Q1108,127 1131,127 H1200 V278 C1170,266 1140,258 1108,254 Z" fill="var(--brand-green)"/>
    <path class="side-panel" d="M1108,240 V150 Q1108,127 1131,127 H1200 V264 C1170,252 1140,244 1108,240 Z" fill="var(--white)"/>

    <path class="feature-shadow" d="M770,127 H1110 V531 Q1110,561 1080,561 H800 Q770,561 770,531 Z" fill="var(--black)"/>
    <path class="feature-box" d="M762,127 H1102 V523 Q1102,553 1072,553 H792 Q762,553 762,523 Z" fill="var(--brand-green)"/>

    <ellipse class="badge-ring" cx="265" cy="455" rx="122" ry="124" fill="var(--brand-green)"/>
    <ellipse class="badge-gap" cx="265" cy="455" rx="114" ry="116" fill="var(--white)"/>
    <ellipse class="badge-core" cx="265" cy="455" rx="108" ry="110" fill="var(--black)"/>

    <g class="icon-pin">
      <ellipse cx="118" cy="720" rx="38" ry="14" fill="none" stroke="var(--white)" stroke-width="6"/>
      <path d="M118,724 C96,692 84,675 84,660 A34,34 0 1 1 152,660 C152,675 140,692 118,724 Z" fill="var(--white)"/>
      <circle cx="118" cy="657" r="12" fill="var(--photo-mid)"/>
    </g>

    <g class="icon-phone-chat" fill="var(--white)">
      <path d="M717,662 C712,668 712,678 718,690 C728,710 744,724 762,730 C772,733 780,731 786,724 L790,719 C792,716 791,712 788,710 L774,701 C771,699 767,700 765,703 L760,709 C750,705 741,696 736,685 L742,680 C745,678 746,674 744,671 L735,657 C733,654 728,653 725,655 Z"/>
      <path d="M760,624 H784 Q798,624 798,638 V648 Q798,662 784,662 H770 L756,673 L758,662 Q746,660 746,648 V638 Q746,624 760,624 Z"/>
      <circle cx="760" cy="643" r="3.5" fill="var(--photo-mid)"/>
      <circle cx="772" cy="643" r="3.5" fill="var(--photo-mid)"/>
      <circle cx="784" cy="643" r="3.5" fill="var(--photo-mid)"/>
    </g>
  </svg>

  <h1 class="business-name">Brackwater Mini Storage</h1>

  <h2 class="headline">Boats, Trailers<br>&amp; RVs Storage</h2>

  <div class="call-now">CALL<br>NOW</div>

  <ul class="features">
    <li>Dry storage<br>spaces</li>
    <li>Self-service<br>facility</li>
    <li>Automatic<br>gate</li>
    <li>24 Hour<br>Access</li>
  </ul>

  <address class="address">218 Harbor Bend Way<br>PO Box 40718<br>Cedar Cove WA 98399</address>

  <div class="contact">
    <div class="contact-label">CALL FOR SPACES</div>
    <div class="contact-phone">360 555 0148</div>
  </div>
</div>
</body>
</html>
```